Real Estate Business Cards

Looking for a clean, sharp and professional look for our Real Estate investment Fund that invests in Multi Family Apartment buildings.

Target Market(s)

Real Estate Fund

Industry/Entity Type

Real Estate

Contact Information for Business Card

Company Description: Real Estate Investment Fund
Company Name: RKW Holdings
Name: Marcus Olvane
Cell: (917) 482-0657
Email: marcus@rkwholdings-example.com
Website: www.rkwholdings-example.com
Address: 418, 9th Street, Brooklyn NY 11218

Colors

Designer to choose colors to be used in the design.

Requirements
Nice to have
• Colors to match logo

```html
<!DOCTYPE html>
<html lang="en">
<head>
<meta charset="utf-8">
<title>RKW Holdings – Business Card</title>
<link rel="stylesheet" href="https://fonts.googleapis.com/css2?family=EB+Garamond:wght@400&family=Roboto:wght@400;500;700&display=swap">
<style>
  :root {
    --backdrop: #c3ae88;
    --card-white: #ffffff;
    --brand-blue: #0b72ad;
    --text-grey: #555555;
    --rule-grey: #6a6a6a;
    --reverse-white: #ffffff;
  }
  * { margin: 0; padding: 0; box-sizing: border-box; }
  html, body { width: 1200px; height: 716px; overflow: hidden; }
  body {
    background: var(--backdrop);
    font-family: "Roboto", Arial, sans-serif;
    position: relative;
  }
  .card {
    position: absolute;
    left: 359px;
    width: 551px;
    height: 314px;
    border-radius: 14px;
    overflow: hidden;
  }
  .card--front { top: 31px; background: var(--card-white); }
  .card--back { top: 367px; background: var(--brand-blue); }

  .wordmark {
    position: absolute;
    display: flex;
    align-items: center;
    gap: 12px;
    font-family: "EB Garamond", Georgia, serif;
    font-weight: 400;
    letter-spacing: 1px;
    white-space: nowrap;
  }
  .wordmark__square { width: 18px; height: 18px; flex: none; }
  .card--front .wordmark { left: 36px; top: 72px; font-size: 36px; color: var(--brand-blue); }
  .card--front .wordmark__square { background: var(--brand-blue); }
  .card--back .wordmark { left: 250px; top: 135px; font-size: 32px; color: var(--reverse-white); }
  .card--back .wordmark__square { background: var(--reverse-white); }

  .holder { position: absolute; left: 148px; top: 143px; }
  .holder__name { font-weight: 700; font-size: 19px; color: var(--brand-blue); letter-spacing: 0.2px; line-height: 22px; }
  .holder__title { font-size: 13px; color: var(--text-grey); line-height: 15px; }

  .divider { position: absolute; left: 148px; top: 184px; width: 372px; height: 1px; background: var(--rule-grey); }

  .contact { position: absolute; left: 148px; top: 192px; color: var(--text-grey); font-size: 13.5px; }
  .contact__company { font-weight: 500; font-size: 14.5px; color: var(--brand-blue); line-height: 18px; }
  .contact__address { line-height: 16px; margin-bottom: 9px; }
  .contact__line { display: flex; align-items: center; gap: 5px; line-height: 17.5px; }
  .contact__icon { width: 12px; height: 12px; flex: none; fill: var(--brand-blue); }
</style>
</head>
<body>
  <section class="card card--front">
    <div class="wordmark"><span class="wordmark__square"></span>RKW HOLDINGS</div>

    <div class="holder">
      <div class="holder__name">MARCUS OLVANE</div>
      <div class="holder__title">Owner</div>
    </div>

    <div class="divider"></div>

    <div class="contact">
      <div class="contact__company">RKW Holdings</div>
      <div class="contact__address">418, 9th Street, Brooklyn NY 11218</div>
      <div class="contact__line">
        <svg class="contact__icon" viewBox="0 0 24 24" aria-hidden="true"><path d="M6.6 10.8a15.1 15.1 0 0 0 6.6 6.6l2.2-2.2a1 1 0 0 1 1-.25 11.4 11.4 0 0 0 3.6.57 1 1 0 0 1 1 1V20a1 1 0 0 1-1 1A17 17 0 0 1 3 4a1 1 0 0 1 1-1h3.5a1 1 0 0 1 1 1c0 1.25.2 2.45.57 3.57a1 1 0 0 1-.25 1z"/></svg>
        (917) 482-0657
      </div>
      <div class="contact__line">
        <svg class="contact__icon" viewBox="0 0 24 24" aria-hidden="true"><path d="M2 5h20v14H2z M3.5 6.5 12 13l8.5-6.5v-0.1H3.5z" fill-rule="evenodd"/><path d="M2 5l10 8 10-8" fill="none" stroke="#fff" stroke-width="1.6"/></svg>
        marcus@rkwholdings-example.com
      </div>
      <div class="contact__line">
        <svg class="contact__icon" viewBox="0 0 24 24" aria-hidden="true"><g fill="none" stroke="#0b72ad" stroke-width="1.8"><circle cx="12" cy="12" r="10"/><ellipse cx="12" cy="12" rx="4.5" ry="10"/><path d="M2 12h20M4 7h16M4 17h16"/></g></svg>
        www.rkwholdings-example.com
      </div>
    </div>
  </section>

  <section class="card card--back">
    <div class="wordmark"><span class="wordmark__square"></span>RKW HOLDINGS</div>
  </section>
</body>
</html>
```